Need Web Page Created

Our company is need to have 3 web pages created (home page, about, contact) using basic html (css is ok). Not looking to use flash or swf, but something that could be used on all browsers and platforms.

I've attached an example design as what we are looking for (as well as logo). The orangish color that is in the logo design should be used on web pages where shown.

Looking for a nice smooth transition between page to page and the page icons up at the top right hand corner should change color based on the page you are viewing (color change can be white or the orangish color from logo).

It Company

```html
<!DOCTYPE html>
<html lang="en">
<head>
<meta charset="utf-8">
<title>Nova Forge Lab</title>
<link rel="stylesheet" href="https://fonts.googleapis.com/css2?family=Quicksand:wght@300;400;500;600&family=Open+Sans:wght@400;600&display=swap">
<style>
  :root {
    --orange: #f39322;
    --orange-soft: #f7a23e;
    --ink: #555555;
    --ink-dark: #3f3f3f;
    --charcoal: #3d3c3d;
    --light: #f4f4f4;
    --white: #ffffff;
    --line: #dddddd;
    --muted: #8a8a8a;
  }
  * { box-sizing: border-box; margin: 0; padding: 0; }
  html, body { width: 706px; height: 1200px; overflow: hidden; }
  body { position: relative; background: var(--light); font-family: "Open Sans", Arial, sans-serif; color: var(--ink); }
  .abs { position: absolute; }

  /* header */
  .site-header { left: 0; top: 0; width: 706px; height: 69px; background: linear-gradient(#ffffff, #f6f6f6); border-bottom: 1px solid #e2e2e2; }
  .brand { left: 70px; top: 22px; display: flex; align-items: center; gap: 6px; font-family: "Quicksand", sans-serif; font-weight: 500; font-size: 19px; color: var(--ink); letter-spacing: .5px; }
  .brand-dot { width: 20px; height: 20px; border-radius: 50%; background: var(--orange); }
  .main-nav { top: 35px; left: 0; width: 706px; font-family: "Quicksand", sans-serif; font-size: 10px; font-weight: 500; color: var(--ink-dark); }
  .main-nav a { position: absolute; color: inherit; text-decoration: none; white-space: nowrap; }

  /* hero */
  .hero { left: 0; top: 69px; width: 706px; height: 320px; background: linear-gradient(#fbfbfb, #ececec); }
  .hero-title { left: 0; top: 36px; width: 706px; text-align: center; font-family: "Quicksand", sans-serif; font-weight: 500; font-size: 25px; color: var(--ink); }
  .hero-title span { color: var(--orange); }
  .hero-sub { left: 0; top: 68px; width: 706px; text-align: center; font-family: "Quicksand", sans-serif; font-size: 13px; color: var(--ink); }
  .hero-art { left: 184px; top: 118px; width: 346px; height: 202px; border-radius: 6px 6px 0 0; background: linear-gradient(135deg, #d9e3ea 0%, #c8d2e4 50%, #e9d7c8 100%); }
  .slider-arrow { top: 134px; }

  /* about */
  .about { left: 0; top: 389px; width: 706px; height: 272px; background: var(--orange); }
  .section-title { left: 0; width: 706px; text-align: center; font-family: "Quicksand", sans-serif; font-weight: 300; font-size: 23px; }
  .about .section-title { top: 32px; color: var(--white); }
  .about-card { top: 80px; width: 279px; height: 156px; background: var(--orange-soft); border-radius: 2px; color: var(--white); text-align: center; padding: 20px 16px 0; }
  .about-card h3 { font-family: "Quicksand", sans-serif; font-weight: 400; font-size: 19px; margin-bottom: 6px; }
  .about-card p { font-size: 7.2px; line-height: 12.2px; }

  /* services */
  .services { left: 0; top: 661px; width: 706px; height: 254px; background-color: var(--charcoal);
    background-image: repeating-linear-gradient(45deg, rgba(255,255,255,.035) 0 1px, transparent 1px 3px); }
  .services .section-title { top: 36px; color: var(--white); font-size: 22px; }
  .service { top: 83px; width: 160px; text-align: center; color: var(--white); }
  .service svg { display: block; margin: 0 auto; }
  .service h4 { font-family: "Quicksand", sans-serif; font-weight: 600; font-size: 11.5px; margin-top: 3px; }
  .service p { font-size: 6.8px; line-height: 11px; color: #d6d6d6; margin-top: 2px; }

  /* contact */
  .contact { left: 0; top: 915px; width: 706px; height: 242px; background: var(--light); overflow: hidden; }
  .contact .section-title { top: 27px; color: var(--ink); font-size: 22px; font-weight: 400; }
  .gear-decor { left: 545px; top: 38px; width: 190px; height: 204px; border-radius: 50% 50% 0 0; background: radial-gradient(circle at 60% 45%, #ffffff 0 55%, #f0f0f0 56%, #f4f4f4 100%); }
  .gear-base { left: 548px; top: 200px; width: 112px; height: 42px; border-radius: 20px 20px 0 0; background: #6b6e6e; }
  .field { position: absolute; background: var(--white); border: 1px solid var(--line); border-radius: 2px; font-size: 7px; color: #666; padding: 6px 8px; }
  .btn { position: absolute; top: 173px; height: 20px; font-family: "Quicksand", sans-serif; font-size: 9.5px; color: var(--white); text-align: center; line-height: 20px; }
  .btn-submit { left: 86px; width: 59px; background: var(--orange); }
  .btn-clear { left: 148px; width: 58px; background: #535353; }
  .map { left: 352px; top: 74px; width: 129px; height: 89px; background: var(--white); border: 1px solid var(--line); padding: 4px; }
  .map div { width: 100%; height: 100%; background: linear-gradient(135deg, #f1e79a 0%, #dfe0d4 55%, #a9c3df 100%); }
  .address { left: 496px; top: 75px; font-size: 7.3px; line-height: 14px; color: #666; }
  .address strong { display: block; font-family: "Quicksand", sans-serif; font-weight: 500; font-size: 9.5px; color: var(--ink-dark); margin-bottom: 1px; }
  .social { left: 497px; top: 147px; display: flex; gap: 6px; }
  .social span { width: 13px; height: 13px; border-radius: 1px; }

  /* footer */
  .site-footer { left: 0; top: 1157px; width: 706px; height: 43px; background: var(--white); }
  .site-footer p { position: absolute; left: 80px; top: 17px; font-size: 7px; color: #555; }
</style>
</head>
<body>

<header class="site-header abs">
  <div class="brand abs"><span>NOVA FORGE LAB</span><span class="brand-dot"></span></div>
  <nav class="main-nav abs">
    <a style="left:371px">HOME</a>
    <a style="left:428px">ABOUT US</a>
    <a style="left:503px">SERVICES</a>
    <a style="left:575px">CONTACT</a>
  </nav>
</header>

<section class="hero abs">
  <h1 class="hero-title abs">Today’s Idea for <span>Tomorrow’s Technology</span></h1>
  <p class="hero-sub abs">Mauris vel lacus vitae felis vestibulum volutpat Etiam est</p>
  <svg class="slider-arrow abs" style="left:33px" width="22" height="46" viewBox="0 0 22 46"><polyline points="21,1 1,23 21,45" fill="none" stroke="#8a8a8a" stroke-width="1.3"/></svg>
  <svg class="slider-arrow abs" style="left:643px" width="22" height="46" viewBox="0 0 22 46"><polyline points="1,1 21,23 1,45" fill="none" stroke="#8a8a8a" stroke-width="1.3"/></svg>
  <div class="hero-art abs" role="img" aria-label="Flat illustration of office technology: tablet with pie charts, desktop monitor with a chart, envelope, pens, wall clock, magnifier and card"></div>
</section>

<section class="about abs">
  <h2 class="section-title abs">About Our Company</h2>
  <article class="about-card abs" style="left:71px">
    <h3>Mission</h3>
    <p>At Nova Forge Lab , our mission is to provide the highest quality solutions to our clients that fits all of their needs. We listen to the client’s needs and find the best solutions with our associates based on skills and background regardless if associate is located remotely or onsite.<br>Nova Forge Lab also believes in treating everyone with respect, integrity and honesty and to exceed client expectations.</p>
  </article>
  <article class="about-card abs" style="left:356px">
    <h3>Experience</h3>
    <p>Nova Forge Lab is an outside‑the‑box thinker for tomorrow’s solutions.<br>We are a technology company that holds several patents for emerging technology with our management team having over 50 combined years on providing solutions.<br>We are also a “think tank”, where no question or idea is ever far‑fetch and the “what‑if” question is a daily occurrence.<br>We are providing solutions on today’s idea for tomorrow’s technology.</p>
  </article>
</section>

<section class="services abs">
  <h2 class="section-title abs">Services Provides</h2>

  <div class="service abs" style="left:107px">
    <svg width="76" height="76" viewBox="0 0 76 76">
      <circle cx="40" cy="40" r="37" fill="none" stroke="#f39322" stroke-width="4" stroke-dasharray="3 2.5" transform="rotate(-200 40 40)" pathLength="360" stroke-dashoffset="0" style="stroke-dasharray:3 2.5"/>
      <circle cx="40" cy="40" r="33" fill="#3d3c3d" stroke="#ffffff" stroke-width="4"/>
      <path d="M35 26h10M37 26v10l-8 14h22l-8-14V26" fill="none" stroke="#fff" stroke-width="2" stroke-linejoin="round"/>
    </svg>
    <h4>Featured Service</h4>
    <p>Etiam est nunc venenatis in tristique eu imperdiet ac nisl Cum sociis natoque pena-tibus et magnis dis parturient</p>
  </div>

  <div class="service abs" style="left:284px">
    <svg width="76" height="76" viewBox="0 0 76 76">
      <circle cx="40" cy="40" r="37" fill="none" stroke="#f39322" stroke-width="4" stroke-dasharray="3 2.5"/>
      <circle cx="40" cy="40" r="33" fill="#3d3c3d" stroke="#ffffff" stroke-width="4"/>
      <circle cx="40" cy="36" r="8" fill="none" stroke="#fff" stroke-width="2"/>
      <path d="M36 46h8M37 50h6M27 36h-4M57 36h-4M40 23v-4" stroke="#fff" stroke-width="2" fill="none"/>
    </svg>
    <h4>Featured Service</h4>
    <p>Etiam est nunc venenatis in tristique eu imperdiet ac nisl Cum sociis natoque pena-tibus et magnis dis parturient</p>
  </div>

  <div class="service abs" style="left:461px">
    <svg width="76" height="76" viewBox="0 0 76 76">
      <circle cx="40" cy="40" r="37" fill="none" stroke="#f39322" stroke-width="4" stroke-dasharray="3 2.5"/>
      <circle cx="40" cy="40" r="33" fill="#3d3c3d" stroke="#ffffff" stroke-width="4"/>
      <circle cx="37" cy="36" r="9" fill="none" stroke="#fff" stroke-width="2.5"/>
      <path d="M43 42l9 9" stroke="#fff" stroke-width="4" stroke-linecap="round"/>
    </svg>
    <h4>Featured Service</h4>
    <p>Etiam est nunc venenatis in tristique eu imperdiet ac nisl Cum sociis natoque pena-tibus et magnis dis parturient</p>
  </div>
</section>

<section class="contact abs">
  <div class="gear-decor abs" role="img" aria-label="Large faint decorative gear shape"></div>
  <div class="gear-base abs" role="img" aria-label="Dark grey decorative gear edge"></div>
  <h2 class="section-title abs">Contact Us</h2>

  <form>
    <div class="field" style="left:84px;top:74px;width:227px;height:20px">Your name</div>
    <div class="field" style="left:85px;top:98px;width:111px;height:20px">Email address</div>
    <div class="field" style="left:199px;top:98px;width:112px;height:20px">Phone</div>
    <div class="field" style="left:85px;top:124px;width:226px;height:44px">Message</div>
    <div class="btn btn-submit">Submit</div>
    <div class="btn btn-clear">Clear</div>
  </form>

  <div class="map abs"><div role="img" aria-label="Street map showing the office location"></div></div>

  <address class="address abs" style="font-style:normal">
    <strong>Nova Forge Lab</strong>
    480 Harbor Lane<br>3rd Floor<br>Riverton, CA 90210<br>Phone (USA): 555-010-4477
  </address>
  <div class="social abs">
    <span style="background:#3b5a9a"></span>
    <span style="background:#3fa9e0"></span>
    <span style="background:#1a6fa5"></span>
    <span style="background:#f07b20"></span>
  </div>
</section>

<footer class="site-footer abs">
  <p>© 2014 Company Name&nbsp; All right reserved&nbsp; Term of Use</p>
</footer>

</body>
</html>
```